Small Accounting Practice needs something creative

We need a business card design for a new small accounting practice based in Perth, Australia. The name of the practice is 'Kelvarin Ledger Group Pty Ltd'. We providing Tax, Bookkeeping and Accounting services. Our target are individuals and small businesses. We want the design to be simply and creative. Also, we can the design can help us to gain people's trust.

Target Market(s)

Individuals and small businesses.

Industry/Entity Type

Accounting

Colors

Designer to choose colors to be used in the design.

```html
<!DOCTYPE html>
<html lang="en">
<head>
<meta charset="utf-8">
<title>Kelvarin Ledger Group – Business Card</title>
<link href="https://fonts.googleapis.com/css2?family=Open+Sans:wght@400;600;700&display=swap" rel="stylesheet">
<style>
  :root {
    --bg: #e9e6e1;
    --card: #ffffff;
    --card-shade: #eeeeee;
    --brand-blue: #1d7fc0;
    --band-blue: #1f4fb0;
    --band-light: #12a6e6;
    --gold: #f2b21b;
    --ink: #2b2b2b;
    --ink-soft: #444444;
    --white: #ffffff;
  }
  * { box-sizing: border-box; margin: 0; padding: 0; }
  html, body { width: 1200px; height: 800px; overflow: hidden; }
  body {
    background: var(--bg);
    font-family: "Open Sans", Arial, sans-serif;
    display: flex; align-items: center; justify-content: center;
  }
  .card {
    position: relative;
    width: 1050px; height: 600px;
    background: radial-gradient(ellipse at 40% 40%, var(--card) 55%, var(--card-shade) 100%);
    box-shadow: 0 10px 30px rgba(0,0,0,.18);
    overflow: hidden;
  }
  .swoosh { position: absolute; inset: 0; width: 100%; height: 100%; }
  .brand {
    position: absolute; left: 60px; top: 118px;
    display: flex; align-items: center; gap: 22px;
  }
  .brand-mark {
    width: 84px; height: 84px; border-radius: 50%;
    background: var(--brand-blue);
  }
  .brand-name {
    color: var(--brand-blue);
    font-weight: 700; font-size: 40px; line-height: 1.05;
  }
  .person {
    position: absolute; right: 60px; top: 52px; text-align: right; color: var(--ink);
  }
  .person-name { font-weight: 700; font-size: 34px; line-height: 1.1; }
  .person-title { font-size: 22px; color: var(--ink-soft); }
  .address {
    position: absolute; right: 60px; top: 220px; text-align: right;
    font-size: 21px; line-height: 1.55; color: var(--ink-soft);
  }
  .contacts {
    position: absolute; left: 68px; top: 332px; list-style: none;
    font-size: 21px; line-height: 1.6; color: var(--ink-soft);
  }
  .contacts li { display: flex; align-items: center; gap: 14px; }
  .contacts svg { width: 20px; height: 20px; fill: var(--ink); }
  .website {
    position: absolute; right: 50px; bottom: 66px;
    color: var(--white); font-size: 32px;
  }
  .website strong { font-weight: 700; }
</style>
</head>
<body>
  <div class="card">
    <svg class="swoosh" viewBox="0 0 1050 600" preserveAspectRatio="none" aria-hidden="true">
      <defs>
        <linearGradient id="band" x1="0" y1="0" x2="1" y2="0">
          <stop offset="0" stop-color="var(--band-blue)"/>
          <stop offset="0.55" stop-color="var(--band-light)"/>
          <stop offset="1" stop-color="var(--band-blue)"/>
        </linearGradient>
        <linearGradient id="goldline" x1="0" y1="0" x2="1" y2="0">
          <stop offset="0" stop-color="var(--gold)"/>
          <stop offset="0.7" stop-color="var(--gold)"/>
          <stop offset="1" stop-color="var(--gold)" stop-opacity="0"/>
        </linearGradient>
      </defs>
      <path d="M0 600 C 330 500 660 380 1000 350 L1050 600 Z" fill="url(#goldline)"/>
      <path d="M20 600 C 360 508 690 396 1050 362 L1050 600 Z" fill="var(--white)"/>
      <path d="M60 600 C 390 522 710 412 1050 374 L1050 600 Z" fill="url(#band)"/>
    </svg>

    <div class="brand">
      <div class="brand-mark"></div>
      <div class="brand-name">Kelvarin Ledger<br>Group</div>
    </div>

    <div class="person">
      <div class="person-name">Daniel Marrow</div>
      <div class="person-title">Managing Director</div>
    </div>

    <div class="address">
      Kelvarin Ledger Group Pty Ltd<br>
      48 Tallow Lane, Suite 12<br>
      Perth, WA 6000
    </div>

    <ul class="contacts">
      <li><svg viewBox="0 0 20 20"><path d="M6 1h8a1 1 0 0 1 1 1v16a1 1 0 0 1-1 1H6a1 1 0 0 1-1-1V2a1 1 0 0 1 1-1zm1 2v12h6V3zm3 13.2a.9.9 0 1 0 0 1.8.9.9 0 0 0 0-1.8z"/></svg>08.6120.4471</li>
      <li><svg viewBox="0 0 20 20"><path d="M5 2h8l2 2v4h2a1 1 0 0 1 1 1v8a1 1 0 0 1-1 1H3a1 1 0 0 1-1-1V9a1 1 0 0 1 1-1h2zm2 2v4h6V5l-1-1zm-2 7v2h2v-2zm4 0v2h2v-2zm4 0v2h2v-2z"/></svg>08.6120.4472</li>
      <li><svg viewBox="0 0 20 20"><path d="M2 6c0-2 4-3 8-3s8 1 8 3v2h-4V6.5c-1-.4-2.5-.6-4-.6s-3 .2-4 .6V8H2zm4 3h8l3 8H3zm4 2a2 2 0 1 0 0 4 2 2 0 0 0 0-4z"/></svg>0412.555.093</li>
      <li><svg viewBox="0 0 20 20"><path d="M2 5h16v10H2zm1.5 1.2V7l6.5 4 6.5-4v-.8z"/></svg>hello@kelvarinledger.au</li>
    </ul>

    <div class="website">www.<strong>kelvarinledger</strong>.au</div>
  </div>
</body>
</html>
```